Business card with logo for a family psychologist

I need a business card for my private practice in the urban Chicago area as a psychologist. I see families and individuals who are going through difficult times - divorce, separation, illness, or trauma. I want to project hopefulness, competence, and caring.

Target Market(s)

Adults, other professionals - such as physicans and lawyers

Industry/Entity Type

Health Care

Contact Information for Business Card

Front should have my name and credentials; back should have location information including my email, phone

Font styles to use
Serif
Decorative
Script

Requirements
Must have
• Unique logo
Should not have
• No pictures or icons of people; no black

```html
<!DOCTYPE html>
<html lang="en">
<head>
<meta charset="UTF-8">
<title>Dana Morrow, Ph.D. — Business Card</title>
<link rel="stylesheet" href="https://fonts.googleapis.com/css2?family=Open+Sans:wght@400;600&family=Marcellus&family=Cinzel:wght@400&display=swap">
<style>
  :root {
    --backdrop: #3a302b;
    --card: #1f2b38;
    --card-edge: #2d3b4a;
    --accent-blue: #3a9be0;
    --accent-green: #8cc63f;
    --text-light: #f2f4f6;
    --silver: #d3d6da;
    --silver-dim: #a3aab2;
    --divider: #34475a;
  }
  * { margin: 0; padding: 0; box-sizing: border-box; }
  html, body { width: 1200px; height: 900px; overflow: hidden; }
  body {
    background: var(--backdrop);
    display: flex;
    align-items: center;
    justify-content: center;
    gap: 60px;
  }
  .card {
    width: 520px;
    height: 300px;
    background: var(--card);
    border: 1px solid var(--card-edge);
    position: relative;
  }

  /* Contact side */
  .card--contact { display: flex; align-items: center; }
  .brand-block {
    width: 250px;
    height: 100%;
    display: flex;
    align-items: center;
    justify-content: center;
    gap: 12px;
    border-right: 1px solid var(--divider);
  }
  .brand-block__mark {
    width: 14px; height: 14px;
    background: var(--accent-green);
  }
  .brand-block__name {
    font-family: "Open Sans", sans-serif;
    font-weight: 600;
    font-size: 26px;
    color: var(--accent-blue);
  }
  .contact {
    padding-left: 30px;
    font-family: "Open Sans", sans-serif;
    color: var(--text-light);
    font-size: 14px;
    line-height: 1.35;
  }
  .contact__name {
    color: var(--accent-blue);
    font-weight: 600;
    font-size: 17px;
  }
  .contact__address { margin-top: 14px; }
  .contact__lines { margin-top: 14px; list-style: none; }
  .contact__lines li { display: flex; align-items: center; gap: 8px; }
  .contact__lines svg { width: 11px; height: 11px; fill: var(--accent-blue); }

  /* Name side */
  .card--name {
    display: flex;
    flex-direction: column;
    align-items: center;
    justify-content: center;
  }
  .name-mark {
    display: flex; align-items: center; gap: 10px;
    font-family: "Marcellus", serif;
    font-size: 22px;
    color: var(--silver-dim);
    margin-bottom: 26px;
  }
  .name-mark__dot {
    width: 10px; height: 10px; border-radius: 50%;
    background: var(--silver-dim);
  }
  .name-title {
    font-family: "Marcellus", serif;
    font-weight: 400;
    font-size: 36px;
    color: var(--silver);
    letter-spacing: 0.5px;
  }
  .name-role {
    font-family: "Cinzel", serif;
    font-size: 13px;
    letter-spacing: 1.5px;
    color: var(--silver-dim);
    margin-top: 4px;
  }
</style>
</head>
<body>
  <section class="card card--contact">
    <div class="brand-block">
      <span class="brand-block__mark"></span>
      <span class="brand-block__name">Dana Morrow</span>
    </div>
    <div class="contact">
      <p class="contact__name">Dana Morrow, Ph.D.</p>
      <p>Licensed Clinical Psychologist</p>
      <p class="contact__address">240 W. Lake Street Suite 310<br>Chicago, Illinois 60606</p>
      <ul class="contact__lines">
        <li>
          <svg viewBox="0 0 24 24" aria-hidden="true"><path d="M6.6 10.8a15 15 0 0 0 6.6 6.6l2.2-2.2a1 1 0 0 1 1-.25 11.4 11.4 0 0 0 3.6.57 1 1 0 0 1 1 1V20a1 1 0 0 1-1 1A17 17 0 0 1 3 4a1 1 0 0 1 1-1h3.5a1 1 0 0 1 1 1c0 1.25.2 2.45.57 3.57a1 1 0 0 1-.25 1z"/></svg>
          312-555-0148
        </li>
        <li>
          <svg viewBox="0 0 24 24" aria-hidden="true"><path d="M2 5h20v14H2z" fill="var(--accent-blue)"/><path d="M3 6l9 7 9-7" stroke="var(--card)" stroke-width="2" fill="none"/></svg>
          drdanamorrow@mail.com
        </li>
      </ul>
    </div>
  </section>

  <section class="card card--name">
    <div class="name-mark">
      <span class="name-mark__dot"></span>
      <span>Dana Morrow</span>
    </div>
    <h1 class="name-title">Dr. Dana Morrow</h1>
    <p class="name-role">Licensed Clinical Psychologist</p>
  </section>
</body>
</html>
```